NORELO - Webdesign für eine Poolreinigungsfirma
Zielgruppe
Wir sind NORELO, eine junge Poolreinigungsfirma die gerade erst in den Startlöchern sitzt. Wir befinden uns auf der französischen Insel LA RÉUNION und richten uns an Personen jeglichen Alters, die einen Pool besitzen.
Aufgabenstellung
Wir wünschen uns ein in erster Linie LUXURIÖSES, schickes und sehr ansprechendes Webdesign, dass - unbedingt - die Verbindung zur Natur zeigt (Tropen, Beispielfotos im Anhang). Natur + Wasser / Pool.
BITTE KEINE TYPISCHE POOLWEBSITE, da wir u.a. auch bald in den Verkauf luxuriöser Accessoires gehen möchten. Wir möchten uns von der Konkurrenz stark und deutlich abheben.
Wir wünschen uns einen DUNKLEN MOOD (gerne auch schwarz auf weißem Hintergrund o.ä. ?).
Wir sind von AI-Bildern sehr angetan, da sie Träume erwecken und in der Tiefe ansprechen können. Nutzen Sie diese gerne, bieten Sie uns Vorschläge. Bitte passend zu den Tropen.
Wir überlassen Ihnen vertrauensvoll die Erstellung des Designs der Website (Aufbau, etc), wir möchten uns überraschen lassen.
Unser Logo, ein Briefing für drei gewünschte Seiten und Beispielbilder, die sehr gerne genutzt werden können (oder in Anlehnung an diese, gleicher Stil) sind im Anhang zu finden.
Die Seite sollte unbedingt - auch - die Nutzung mit Mobiltelefonen ermöglichen und keine Verzögerungen beim Aufrufen / Laden der Website aufzeigen.

```html
<!DOCTYPE html>
<html lang="fr">
<head>
<meta charset="utf-8">
<title>NORELO – Expériences</title>
<link rel="stylesheet" href="https://fonts.googleapis.com/css2?family=Playfair+Display:wght@700;800&family=Manrope:wght@400;500;700&display=swap">
<style>
  :root {
    --bg: #000000;
    --text: #ffffff;
    --accent-teal: #56b8b2;
    --frame-blue: #2c95c8;
    --map-sea: #a7c2c0;
    --map-land: #dfe2d4;
  }
  * { margin: 0; padding: 0; box-sizing: border-box; }
  html, body { width: 1200px; height: 887px; overflow: hidden; background: var(--bg); }
  body { position: relative; color: var(--text); font-family: "Manrope", sans-serif; }

  .brand {
    position: absolute; left: 95px; top: 0;
    font-family: "Manrope", sans-serif; font-weight: 400;
    font-size: 22px; letter-spacing: 6px; line-height: 1;
  }
  .main-nav { position: absolute; top: 0; left: 729px; height: 14px; }
  .main-nav a {
    position: absolute; top: 0; color: var(--text); text-decoration: none;
    font-weight: 700; font-size: 11.5px; white-space: nowrap; line-height: 1;
  }
  .main-nav .nav-main { left: 0; }
  .main-nav .nav-contact { left: 74px; }
  .main-nav .nav-about { left: 168px; }

  .heading {
    font-family: "Playfair Display", serif; font-weight: 800;
    letter-spacing: -1px; line-height: 1; white-space: nowrap;
  }
  .lede { font-size: 11.5px; line-height: 1; white-space: nowrap; }

  .experiences-title { position: absolute; right: 557px; top: 49px; font-size: 35px; }
  .experiences-line { position: absolute; right: 560px; }
  .experiences-line.l1 { top: 113px; }
  .experiences-line.l2 { top: 138px; }

  .slash-rule {
    position: absolute; height: 9px;
    background: repeating-linear-gradient(90deg, var(--accent-teal) 0 1px, transparent 1px 3.2px);
    transform: skewX(-25deg);
  }
  .slash-rule.first { left: 22px; width: 640px; top: 192px; }
  .slash-rule.second { left: 2px; width: 478px; top: 388px; }

  .trust-title { position: absolute; left: 20px; top: 244px; font-size: 35px; }
  .trust-line { position: absolute; left: 20px; }
  .trust-line.l1 { top: 308px; }
  .trust-line.l2 { top: 332px; }

  .hero-visual { position: absolute; left: 0; top: 0; width: 1200px; height: 887px; pointer-events: none; }

  .contact-panel {
    position: absolute; left: 154px; top: 669px; width: 1041px; height: 260px;
    border: 2.5px solid var(--frame-blue);
  }
  .contact-title { position: absolute; left: 22px; top: 30px; font-size: 34px; letter-spacing: -1.5px; }
  .contact-details { position: absolute; left: 22px; top: 93px; list-style: none; }
  .contact-details li { font-size: 12px; line-height: 24px; }
  .location-map {
    position: absolute; left: 531px; top: 21px; width: 485px; height: 240px;
    background: linear-gradient(135deg, var(--map-sea) 0%, var(--map-land) 55%, var(--map-sea) 100%);
  }
</style>
</head>
<body>
  <header>
    <div class="brand">NORELO</div>
    <nav class="main-nav">
      <a class="nav-main" href="#">MAIN</a>
      <a class="nav-contact" href="#">CONTACT</a>
      <a class="nav-about" href="#">ABOUT US</a>
    </nav>
  </header>

  <svg class="hero-visual" viewBox="0 0 1200 887" role="img" aria-label="Photo: hands floating in clear turquoise pool water">
    <defs>
      <linearGradient id="poolTones" x1="0" y1="0" x2="1" y2="1">
        <stop offset="0" stop-color="#4a8f98"/>
        <stop offset="0.45" stop-color="#c99478"/>
        <stop offset="0.75" stop-color="#7a5a48"/>
        <stop offset="1" stop-color="#6fa9b0"/>
      </linearGradient>
    </defs>
    <path d="M848,50 H1200 V527 C1110,512 1000,482 930,442 C860,400 799,330 799,225 C799,150 818,92 848,50 Z" fill="url(#poolTones)"/>
  </svg>

  <section class="experiences">
    <h2 class="heading experiences-title">EXPÉRIENCES</h2>
    <p class="lede experiences-line l1">Riche d’une expérience de 20 ans, nous nous adressons</p>
    <p class="lede experiences-line l2">aux particuliers, professionnels, location saisonnière et bien plus.</p>
    <div class="slash-rule first" aria-hidden="true"></div>
  </section>

  <section class="trust">
    <h2 class="heading trust-title">CONFIANCE</h2>
    <p class="lede trust-line l1">Libérez-vous des soucis et contraintes liées à la possession de</p>
    <p class="lede trust-line l2">votre piscine, nous sommes là pour vous accompagner avec professionnalisme.</p>
    <div class="slash-rule second" aria-hidden="true"></div>
  </section>

  <section class="contact-panel">
    <h2 class="heading contact-title">CONTACT NORELO</h2>
    <ul class="contact-details">
      <li>Adresse domiciliation</li>
      <li>Mail : contact@norelo.re</li>
      <li>téléphone : 0692.41.86.27</li>
    </ul>
    <div class="location-map" role="img" aria-label="Map of La Réunion island showing the service area"></div>
  </section>
</body>
</html>
```